Moro Leb Bottling Project needs a Food-Wine Label (front & back) design

We have an approved label for 20L kegs that match with the company name. Now we need to make another label (5 x 3.5 in) more attractive to be used in bottles. We are going to bottling (750ML) wine from kegs. We want to keep, if possible, a relation between both labels, such as the color, appeal to the concept of freshness, directly from the vineyard to your glass, eco-friendly, elegant/ artistic, new way of drinking, the solution or path to the future. We drafted a label with our vision so you can be inspired and complete our idea. Brand is Luz Quieta (still light), varietal and vintage as well as volume are changeable. Company logo is also included for your reference and we would like to be included in the back label or part of it, and also the phrase Moss Wine is another element that we used for our marketing. Any further information contact us.

```html
<!DOCTYPE html>
<html lang="en">
<head>
<meta charset="utf-8">
<title>Luz Quieta Chardonnay — Bottle Labels</title>
<link href="https://fonts.googleapis.com/css2?family=Marcellus&family=EB+Garamond:ital,wght@0,400;1,400&family=Montserrat:wght@500;600;700&display=swap" rel="stylesheet">
<style>
  :root {
    --gold: #d9b65a;
    --gold-deep: #b8933a;
    --gold-soft: #e6c877;
    --label-black: #000000;
    --panel-black: #0a0a0b;
    --paper: #ffffff;
    --ink: #1a1a1a;
    --page: #ffffff;
  }
  * { box-sizing: border-box; margin: 0; padding: 0; }
  html, body { width: 865px; height: 1200px; overflow: hidden; background: var(--page); }
  .canvas { position: relative; width: 865px; height: 1200px; overflow: hidden; background: var(--page); }

  /* ---------- Front label ---------- */
  .front-label {
    position: absolute; left: 83px; top: 88px; width: 309px; height: 441px;
    background: var(--label-black);
  }
  .front-label .frame {
    position: absolute; left: 26px; top: 27px; width: 257px; height: 388px;
    border: 1.2px solid var(--gold);
  }
  .front-label .panel {
    position: absolute; left: 29px; top: 109px; width: 211px; height: 306px;
    background: var(--panel-black);
  }
  .front-label .varietal-tab {
    position: absolute; left: 116px; top: 0; width: 136px; height: 82px;
    background: linear-gradient(160deg, var(--gold-soft), var(--gold) 55%, var(--gold-deep));
  }
  .front-label .varietal {
    position: absolute; left: 116px; top: 67px; width: 136px; text-align: center;
    font-family: "Montserrat", sans-serif; font-weight: 500; font-size: 7.6px;
    letter-spacing: 3.6px; color: var(--ink);
  }
  .front-label .artwork {
    position: absolute; left: 32px; top: 126px; width: 80px; height: 286px;
    background: linear-gradient(180deg, var(--gold-soft) 0%, var(--gold) 55%, var(--gold-deep) 100%);
  }
  .front-label .brand {
    position: absolute; left: 120px; top: 124px;
    font-family: "Marcellus", serif; font-weight: 400; font-size: 38px; line-height: 38px;
    color: var(--gold); letter-spacing: 0;
  }
  .front-label .tagline {
    position: absolute; left: 123px; top: 219px;
    font-family: "Montserrat", sans-serif; font-weight: 500; font-size: 9.5px;
    letter-spacing: 4.8px; color: var(--gold);
  }
  .front-label .vintage {
    position: absolute; left: 218px; top: 386px;
    font-family: "EB Garamond", serif; font-style: italic; font-size: 13px;
    letter-spacing: 4px; color: var(--gold);
  }

  /* ---------- Back label ---------- */
  .back-label {
    position: absolute; left: 78px; top: 599px; width: 309px; height: 341px;
    background: var(--label-black);
  }
  .back-label .sheet {
    position: absolute; left: 16px; top: 16px; width: 281px; height: 310px;
    background: var(--paper); border: 1.2px solid var(--gold);
  }
  .back-label .varietal-tab {
    position: absolute; left: 96px; top: 4px; width: 125px; height: 24px;
    background: linear-gradient(160deg, var(--gold-soft), var(--gold) 55%, var(--gold-deep));
  }
  .back-label .content {
    position: absolute; left: 16px; top: 16px; width: 281px; height: 310px;
    color: var(--ink); text-align: center;
  }
  .back-label .title {
    margin-top: 19px;
    font-family: "Montserrat", sans-serif; font-weight: 700; font-size: 8.2px;
    letter-spacing: 2.6px;
  }
  .back-label .origin {
    margin-top: 9px;
    font-family: "EB Garamond", serif; font-size: 8.2px; font-variant: small-caps; letter-spacing: 0.2px;
  }
  .back-label .tasting-notes {
    margin: 9px 12px 0;
    font-family: "EB Garamond", serif; font-style: italic; font-size: 8.8px;
    line-height: 11px; text-align: justify;
  }
  .back-label .producer {
    position: absolute; left: 42px; top: 188px; display: flex; align-items: center; gap: 8px;
    text-align: left;
  }
  .back-label .producer-mark {
    display: flex; align-items: center; gap: 3px;
    font-family: "EB Garamond", serif; font-size: 8px; color: var(--ink);
  }
  .back-label .producer-mark .dot {
    width: 8px; height: 8px; border-radius: 50%; background: var(--gold);
  }
  .back-label .producer-text {
    font-family: "EB Garamond", serif; font-size: 8px; line-height: 11px;
  }
  .back-label .specs {
    position: absolute; left: 14px; right: 14px; top: 228px;
    display: flex; justify-content: space-between;
    font-family: "Montserrat", sans-serif; font-weight: 600; font-size: 7px; letter-spacing: 0.3px;
  }
  .back-label .warning {
    position: absolute; left: 10px; right: 10px; top: 247px;
    font-family: "EB Garamond", serif; font-size: 6.3px; line-height: 8.6px; text-transform: uppercase;
    letter-spacing: -0.1px;
  }
  .back-label .footer {
    position: absolute; left: 36px; right: 36px; top: 297px;
    display: flex; justify-content: space-between;
    font-family: "Montserrat", sans-serif; font-weight: 600; font-size: 5.4px; letter-spacing: 0.3px;
  }
</style>
</head>
<body>
<main class="canvas">

  <section class="front-label" aria-label="Front label">
    <div class="frame"></div>
    <div class="panel"></div>
    <div class="varietal-tab" role="img" aria-label="Gold block with flowing contour-line pattern"></div>
    <div class="varietal">CHARDONNAY</div>
    <div class="artwork" role="img" aria-label="Gold illustration of wine flowing into vineyard rows"></div>
    <h1 class="brand">LUZ<br>QUIETA</h1>
    <div class="tagline">VINO DE MUSGO</div>
    <div class="vintage">2017</div>
  </section>

  <section class="back-label" aria-label="Back label">
    <div class="sheet"></div>
    <div class="varietal-tab" role="img" aria-label="Gold block with flowing contour-line pattern"></div>
    <div class="content">
      <h2 class="title">2017 CHARDONNAY</h2>
      <p class="origin">Light French Oak – Yakima Valley, WA</p>
      <p class="tasting-notes">“Aromas of honeysuckle, melon, flowers, toasted cashews… Ripe pears and lemons, crispy fresh acidity expressed in mouth… Elegant subtle creaminess finish with a touch of exotic oak spices… Fermented in stainless-steel followed by a partial malolactic fermentation in French oak barrels, rendering a nicely balanced Chardonnay with great structure, bright and abundant in fruit aromas. Ideal for pairing with poultry (chicken, guinea…), fish (salmon, codfish…) in lightly spiced buttery sauces, creamy pasta dishes, fresh veggie salads and soft-to-mild cheeses. Cheers!”</p>
      <div class="producer">
        <div class="producer-mark"><span class="dot"></span><span>Moro Leb</span></div>
        <p class="producer-text">Packed by ,<br>PR and distributed by MLBP, Bahía Clara, PR</p>
      </div>
      <div class="specs"><span>CONTAIN SULFITES</span><span>750ML</span><span>ALC. 13.5% BY VOL.</span></div>
      <p class="warning">Government warning: (1) According to the Surgeon General, women should not drink alcoholic beverages during pregnancy because of the risk of birth defects. (2) Consumption of alcoholic beverages impairs your availability to drive a car or operate machinery, and may cause health problems.</p>
      <div class="footer"><span>ECO-FRIENDLY</span><span>@MLBPPR</span><span>@mosswine</span><span>VEGAN</span></div>
    </div>
  </section>

</main>
</body>
</html>
```